Business Reporting Graph Illustration

I'm looking for a graphic design to created an illustration of a line chart I have two sample charts that I'd like elements of each combined together to create the project. Below is a link to learn more about this project. This should be designed using any product of the Adobe Suite.
Color Scheme is included within the below link. This will require 2 - 3 rounds of design before final completion.

https://www.plonvadesk.com/file/QWT8HbxuLeMRa302KD5Vpt/Graphic-Design-Project

```html
<!DOCTYPE html>
<html lang="en">
<head>
<meta charset="utf-8">
<title>Business Reporting Graph</title>
<link rel="stylesheet" href="https://fonts.googleapis.com/css2?family=Arimo:wght@400&display=swap">
<style>
  :root {
    --bg-start: #f3f3f3;
    --bg-end: #ffffff;
    --ink: #1c1e3a;
    --axis-blue: #5a7db5;
    --ad-orange: #f7ae26;
    --label-white: #ffffff;
  }
  html, body {
    margin: 0;
    padding: 0;
    width: 1200px;
    height: 609px;
    overflow: hidden;
  }
  body {
    background: linear-gradient(135deg, var(--bg-end) 0%, var(--bg-start) 100%);
    font-family: "Arimo", Arial, sans-serif;
  }
  .chart {
    display: block;
    width: 1200px;
    height: 609px;
  }
  .axis-line { stroke: var(--ink); stroke-width: 4; }
  .axis-tick { stroke: var(--axis-blue); stroke-width: 4; }
  .axis-label, .axis-title { fill: var(--axis-blue); font-size: 40px; }
  .series-line {
    fill: none; stroke: var(--ink); stroke-width: 6;
    stroke-linejoin: round; stroke-linecap: round;
  }
  .baseline-line {
    fill: none; stroke: var(--axis-blue); stroke-width: 7;
    stroke-dasharray: 14 10; stroke-linecap: round;
  }
  .ad-window { stroke: var(--ad-orange); stroke-width: 4; stroke-dasharray: 8 6; }
  .ad-badge { fill: var(--ad-orange); }
  .ad-badge-text { fill: var(--label-white); font-size: 40px; text-anchor: middle; }
  .ad-duration { fill: var(--ink); font-size: 25px; text-anchor: middle; }
  .ad-span { stroke: var(--ad-orange); stroke-width: 3; }
  .ad-span-head { fill: var(--ad-orange); }
</style>
</head>
<body>
<svg class="chart" viewBox="0 0 2576 1308" xmlns="http://www.w3.org/2000/svg" role="img" aria-label="Line chart of response per minute from 10:00 am to 1:30 pm with spikes after two TV ads and one radio ad">

  <!-- Ad windows -->
  <g class="ad-windows">
    <line class="ad-window" x1="962" y1="375" x2="962" y2="1092"/>
    <line class="ad-window" x1="1080" y1="375" x2="1080" y2="1092"/>
    <line class="ad-window" x1="1658" y1="375" x2="1658" y2="1092"/>
    <line class="ad-window" x1="1742" y1="375" x2="1742" y2="1092"/>
    <line class="ad-window" x1="2044" y1="375" x2="2044" y2="1092"/>
    <line class="ad-window" x1="2120" y1="375" x2="2120" y2="1092"/>
  </g>

  <!-- Ad labels -->
  <g class="ad-label">
    <rect class="ad-badge" x="937" y="263" width="170" height="57"/>
    <text class="ad-badge-text" x="1022" y="305">TV Ad</text>
    <text class="ad-duration" x="1022" y="353">10 min</text>
    <line class="ad-span" x1="1004" y1="367" x2="1040" y2="367"/>
    <path class="ad-span-head" d="M994 367 L1008 360 L1008 374 Z M1050 367 L1036 360 L1036 374 Z"/>
  </g>
  <g class="ad-label">
    <rect class="ad-badge" x="1617" y="263" width="170" height="57"/>
    <text class="ad-badge-text" x="1702" y="305">TV Ad</text>
    <text class="ad-duration" x="1702" y="350">5 min</text>
    <line class="ad-span" x1="1684" y1="367" x2="1720" y2="367"/>
    <path class="ad-span-head" d="M1674 367 L1688 360 L1688 374 Z M1730 367 L1716 360 L1716 374 Z"/>
  </g>
  <g class="ad-label">
    <rect class="ad-badge" x="1990" y="263" width="192" height="57"/>
    <text class="ad-badge-text" x="2086" y="306">Radio Ad</text>
    <text class="ad-duration" x="2086" y="350">3 min</text>
    <line class="ad-span" x1="2068" y1="367" x2="2104" y2="367"/>
    <path class="ad-span-head" d="M2058 367 L2072 360 L2072 374 Z M2114 367 L2100 360 L2100 374 Z"/>
  </g>

  <!-- Expected baseline during ads -->
  <g class="baselines">
    <path class="baseline-line" d="M946 962 C960 985 972 1000 990 990 C1005 982 1015 968 1024 976 C1035 990 1045 1012 1060 1002 C1075 992 1085 985 1095 978"/>
    <path class="baseline-line" d="M1628 1005 C1650 998 1672 985 1688 992 C1700 1000 1712 1025 1728 1026 C1742 1026 1752 1010 1760 1002"/>
    <path class="baseline-line" d="M2020 993 C2045 996 2070 1000 2095 1004 C2108 1004 2114 990 2122 980"/>
  </g>

  <!-- Response series -->
  <polyline class="series-line" points="308,1018 372,976 421,1016 476,965 560,992 626,1027 694,930 767,1014 804,992 852,1011 932,944 962,970 1022,558 1080,980 1158,924 1211,994 1247,954 1300,1028 1356,1002 1374,975 1431,987 1465,1026 1506,975 1548,1028 1658,995 1697,520 1737,1020 1850,906 1883,978 1926,947 1955,980 2050,996 2078,745 2118,982 2208,895 2274,1014 2300,1014 2358,1046 2383,984 2430,1034"/>

  <!-- Time axis -->
  <g class="time-axis">
    <line class="axis-line" x1="272" y1="1096" x2="2472" y2="1096"/>
    <line class="axis-tick" x1="308" y1="1098" x2="308" y2="1120"/>
    <line class="axis-tick" x1="500" y1="1098" x2="500" y2="1120"/>
    <line class="axis-tick" x1="693" y1="1098" x2="693" y2="1120"/>
    <line class="axis-tick" x1="886" y1="1098" x2="886" y2="1120"/>
    <line class="axis-tick" x1="1079" y1="1098" x2="1079" y2="1120"/>
    <line class="axis-tick" x1="1272" y1="1098" x2="1272" y2="1120"/>
    <line class="axis-tick" x1="1465" y1="1098" x2="1465" y2="1120"/>
    <line class="axis-tick" x1="1658" y1="1098" x2="1658" y2="1120"/>
    <line class="axis-tick" x1="1851" y1="1098" x2="1851" y2="1120"/>
    <line class="axis-tick" x1="2044" y1="1098" x2="2044" y2="1120"/>
    <line class="axis-tick" x1="2237" y1="1098" x2="2237" y2="1120"/>
    <line class="axis-tick" x1="2430" y1="1098" x2="2430" y2="1120"/>
    <text class="axis-title" x="64" y="1112">Minutes</text>
    <text class="axis-label" x="232" y="1170">10:00 am</text>
    <text class="axis-label" x="812" y="1170">11:00 am</text>
    <text class="axis-label" x="1389" y="1170">12:00 am</text>
    <text class="axis-label" x="1986" y="1170">1:00 pm</text>
  </g>
</svg>
</body>
</html>
```